teaching love. a joyful state of being.

adding value to ones circumstance through the teachings of neutralization. quote for back of card: "and then it happens... One day you wake up and you're in this place. You are in this place where everything is right. Your heart is calm. Your soul is lit. Your thoughts are positive. Your vision is clear. Your faith is stronger than ever. And you are at peace. At peace with where you have been. At peace with what you've been through. And at peace with where you're headed." -unknown

Target Market(s)

spiritual, awakening, inspiration, motivation, gratefulness, oneness, peace, positive mindset,

Contact Information for Business Card

front: one line message from quote

Logo Text

up to suggestions

Font styles to use
Serif
Sans Serif
Script

Colors

Designer to choose colors to be used in the design.

Requirements
Must have
• entire quote on one side of card
Nice to have
• simple, and to the point
Should not have
• elaborated designs

```html
<!DOCTYPE html>
<html lang="en">
<head>
<meta charset="utf-8">
<title>Teaching Love – Business Card</title>
<link rel="stylesheet" href="https://fonts.googleapis.com/css2?family=Petit+Formal+Script&family=Cormorant+Garamond:wght@400&family=Poppins:wght@200;300&display=swap">
<style>
  :root {
    --page-bg: #e9e7e3;
    --card-bg: #2a201e;
    --gold: #caa12f;
    --gold-soft: #b8912a;
  }
  * { box-sizing: border-box; margin: 0; padding: 0; }
  html, body {
    width: 1200px;
    height: 1021px;
    overflow: hidden;
    background: var(--page-bg);
  }
  .sheet {
    width: 1200px;
    height: 1021px;
    display: flex;
    flex-direction: column;
    align-items: center;
    justify-content: center;
    gap: 60px;
  }
  .card {
    position: relative;
    width: 700px;
    height: 400px;
    background: var(--card-bg);
    box-shadow: 0 6px 18px rgba(0, 0, 0, 0.18);
    color: var(--gold);
    overflow: hidden;
  }

  /* Quote side */
  .quote {
    position: absolute;
    left: 50px;
    top: 118px;
    width: 470px;
    font-family: "Petit Formal Script", cursive;
    font-size: 12.5px;
    line-height: 2.15;
  }
  .quote-line { display: block; white-space: nowrap; }
  .quote-author {
    position: absolute;
    right: 38px;
    top: 128px;
    font-family: "Cormorant Garamond", serif;
    font-size: 18px;
    letter-spacing: 1.2px;
    white-space: nowrap;
  }

  /* Hashtag side */
  .tags-side {
    display: flex;
    flex-direction: column;
    align-items: center;
    justify-content: center;
  }
  .rule {
    display: block;
    width: 92px;
    height: 2px;
    background: var(--gold);
  }
  .rule-top { margin-bottom: 26px; transform: translateX(-28px); }
  .rule-bottom { margin-bottom: 40px; transform: translateX(28px); }
  .tags {
    font-family: "Poppins", sans-serif;
    font-size: 25px;
    letter-spacing: 0.3px;
    white-space: nowrap;
  }
  .tags-strong { font-weight: 300; }
  .tags-light { font-weight: 200; color: var(--gold-soft); }
</style>
</head>
<body>
  <main class="sheet">
    <section class="card quote-side" aria-label="Card back with quote">
      <p class="quote">
        <span class="quote-line">“and then it happens... One day you wake up and you’re in this place.</span>
        <span class="quote-line">You are in this place where everything is right. Your heart is calm.</span>
        <span class="quote-line">Your soul is lit. Your thoughts are positive. Your vision is clear.</span>
        <span class="quote-line">Your faith is stronger than ever. And you are at peace. At peace with</span>
        <span class="quote-line">where you have been. At peace with what you’ve been through. And at</span>
        <span class="quote-line">peace with where you’re headed.”</span>
      </p>
      <p class="quote-author">-UNKNOWN</p>
    </section>

    <section class="card tags-side" aria-label="Card front with hashtags">
      <span class="rule rule-top"></span>
      <span class="rule rule-bottom"></span>
      <p class="tags">
        <span class="tags-strong">#spiritual, #aware, #love</span>
        <span class="tags-light">#loveguru #lenaharwood</span>
      </p>
    </section>
  </main>
</body>
</html>
```